Luxury Corporate Wellness Brochure | Still Harbor Tone Soak

We are looking for a graphic designer to create a premium tri-fold (or other folding brochure, open to elevated formats beyond a trifold) brochure (print + digital PDF) for our corporate wellness brand, Still Harbor Tone Soak.
The brochure will be shared with hotel sales managers, conference services teams, destination management companies (DMCs), and corporate meeting planners throughout Southern California.
Our goal is to position Still Harbor as a luxury wellness partner for conferences, executive retreats, incentive travel, and corporate events.
The brochure should introduce our services, including:
Reset Rooms (dedicated wellness spaces during conferences)
Guided Meditation
Breathwork
Yoga (including chair yoga)
Private Floating Sound Bath experiences
Executive retreat wellness programming
This is not a spa brochure or yoga studio flyer. It should feel like a piece created for a luxury hotel brand.
Design Direction
The design should feel elegant, sophisticated, and editorial.
Think:
Telvo Resorts
Nine Pines Gatherings
Brindle-Hollow Party Sales
Calloway Resorts
Marlpine Hotels
Avoid common AI-generated design trends such as:
Purple and teal gradients
Lotus flowers
Stacked stones
Watercolor textures
Dreamcatchers
Mandalas
Generic meditation silhouettes
Overused wellness clichés
The design should rely on:
Beautiful typography
Strong photography
Clean layouts
Generous white space
Minimal icons
A luxury hospitality aesthetic
Deliverables
Print-ready tri-fold brochure (CMYK)
Editable source file (Adobe InDesign preferred)
Press-ready PDF
Digital PDF optimized for email
Assets Provided
I will provide:
Brand logo
Professional photography
Brand colors
Copy/content
Contact information
The designer is welcome to recommend layout improvements while maintaining a premium, hospitality-focused aesthetic.
Overall Goal
The finished brochure should be something a luxury resort sales director would confidently hand to a Pinnacle 700 meeting planner. It should communicate professionalism, exclusivity, and the value of incorporating wellness into corporate events while showcasing Still Harbor Tone Soak as a trusted hospitality partner.

```html
<!DOCTYPE html>
<html lang="en">
<head>
<meta charset="utf-8">
<title>Still Harbor Tone Soak — Tri-fold Brochure</title>
<link rel="stylesheet" href="https://fonts.googleapis.com/css2?family=Gilda+Display&family=Inter:wght@300;400&family=Cormorant+Garamond:ital,wght@1,400&display=swap">
<style>
  :root{
    --stage:#a9a9a9;
    --navy:#131d30;
    --navy-mid:#16223a;
    --gold:#b8955a;
    --brand-blue:#2b7cc6;
    --text:#d9dde4;
    --text-soft:#c3c8d1;
    --rule:#2c3850;
  }
  *{margin:0;padding:0;box-sizing:border-box}
  html,body{width:869px;height:1200px;overflow:hidden;background:var(--stage)}
  body{position:relative;font-family:"Inter",sans-serif;color:var(--text)}
  .spread{position:absolute;left:38px;width:791px;height:554px;overflow:hidden;background:var(--navy);box-shadow:2px 3px 6px rgba(0,0,0,.35)}
  .spread--outside{top:38px}
  .spread--inside{top:607px}
  .panel{position:absolute;top:0;height:100%;width:263px}
  .abs{position:absolute}
  .serif{font-family:"Gilda Display",serif;font-weight:400;letter-spacing:.04em}
  .center{text-align:center}
  .gold{color:var(--gold)}
  .rule{position:absolute;height:1px;background:var(--gold)}
  .photo{position:absolute}
  .body-copy{font-size:8.2px;line-height:13.3px;font-weight:300;color:var(--text)}
  .brand{font-family:"Inter",sans-serif;font-weight:400;color:var(--brand-blue);letter-spacing:.12em;text-align:center;line-height:1.15}

  /* outside spread */
  .panel--back{left:0}
  .panel--back .photo{inset:0;background:linear-gradient(180deg,#0d1930 0%,#1a2a44 35%,#2a3140 55%,#143a6e 75%,#1c6fc8 100%)}
  .panel--contact{left:263px;width:264px;background:var(--navy-mid)}
  .panel--cover{left:527px;width:264px;background:var(--navy)}
  .panel--cover .photo{left:0;right:0;top:214px;bottom:0;background:linear-gradient(180deg,#1a2a3c 0%,#5a4a2c 30%,#2d6a78 60%,#1b8fa6 85%,#0f4e63 100%)}
  .contact-list{position:absolute;left:48px;top:410px;list-style:none}
  .contact-list li{display:flex;align-items:center;height:20.3px;font-size:8.3px;font-weight:300;color:var(--text)}
  .contact-list svg{width:10px;height:10px;margin-right:10px;flex:none}
  .wave-field{position:absolute;left:0;right:0;bottom:0;height:95px;background:linear-gradient(170deg,rgba(22,34,58,0) 20%,rgba(40,90,160,.25) 60%,rgba(43,124,198,.4) 100%)}

  /* inside spread */
  .bottom-photo{left:0;top:293px;width:527px;height:261px;background:linear-gradient(180deg,#151b2a 0%,#3a2c2a 30%,#4a3a30 45%,#1c4f86 62%,#2b2d4a 80%,#1a1a2c 100%)}
  .side-photo{left:697px;top:0;width:94px;height:554px;background:linear-gradient(180deg,#c9ccd0 0%,#8a8f96 20%,#3c4048 45%,#2a3450 70%,#2f7ca0 100%)}
  .portrait{left:337px;top:24px;width:116px;height:116px;border-radius:50%;background:radial-gradient(circle at 40% 40%,#d88ad8 0%,#9c3ea8 45%,#4a2050 100%)}
  .section-title{font-size:17px;line-height:24px;color:var(--text)}
  .quote-mark{font-family:"Gilda Display",serif;font-size:56px;line-height:1;color:var(--gold)}
  .quote{font-family:"Cormorant Garamond",serif;font-style:italic;font-size:15.5px;line-height:17.5px;color:var(--gold)}
  .service-icon{position:absolute;left:543px;width:13px;height:13px;border:1px solid var(--gold);border-radius:50%}
  .service-title{position:absolute;left:573px;font-weight:400;font-size:9.8px;line-height:12px;letter-spacing:.02em;color:var(--gold);white-space:nowrap}
  .service-copy{position:absolute;left:573px;width:112px;font-size:8.2px;line-height:10.8px;font-weight:300;color:var(--text)}
  .sep{position:absolute;left:546px;width:118px;height:1px;background:var(--rule)}
  .cta-title{left:546px;top:452px;font-size:12px;line-height:16px;color:var(--gold);white-space:nowrap}
  .cta-copy{left:546px;top:489px;font-size:9.4px;line-height:12px;color:var(--text);width:214px}
</style>
</head>
<body>

<section class="spread spread--outside">
  <div class="panel panel--back">
    <div class="photo" role="img" aria-label="Night poolside sound bath with guests lying on floats, umbrellas and mountains behind"></div>
    <h1 class="abs serif center" style="left:0;width:263px;top:95px;font-size:17px;line-height:24px;color:var(--text)">RESET.<br>RECHARGE.<br>PERFORM.</h1>
    <div class="rule" style="left:116px;top:182px;width:32px"></div>
    <p class="abs center body-copy" style="left:0;width:263px;top:194px">Thoughtful wellness experiences<br>that elevate people, performance<br>and every moment in between.</p>
    <p class="abs center" style="left:0;width:263px;top:504px;font-size:8px;line-height:14px;font-weight:300;color:var(--text)">STILLHARBORTONESOAK.COM<br>Southern, California</p>
  </div>

  <div class="panel panel--contact">
    <div class="abs brand" style="left:0;width:264px;top:88px;font-size:17px">STILL HARBOR<br><span style="font-size:10px">TONE SOAK</span></div>
    <div class="rule" style="left:116px;top:150px;width:33px"></div>
    <p class="abs center body-copy" style="left:0;width:264px;top:169px">We partner with luxury hotels, resorts<br>and conference venues to deliver seamless,<br>high-impact wellness experiences for<br>corporate events, retreats and incentives.</p>
    <div class="rule" style="left:116px;top:241px;width:33px"></div>
    <div class="wave-field" role="img" aria-label="Flowing fine-line wave pattern"></div>
    <ul class="contact-list">
      <li><svg viewBox="0 0 10 10"><path d="M2 1l2 2-1 1.3c.6 1.2 1.5 2.1 2.7 2.7L7 6l2 2-1.3 1.5C4.5 9.3.7 5.5.5 2.3z" fill="var(--gold)"/></svg>(555) 014-2290</li>
      <li><svg viewBox="0 0 10 10"><rect x=".5" y="2" width="9" height="6.5" fill="var(--gold)"/><path d="M.5 2l4.5 3.5L9.5 2" stroke="var(--navy-mid)" stroke-width=".8" fill="none"/></svg>hello@stillharbortonesoak.com</li>
      <li><svg viewBox="0 0 10 10" fill="none" stroke="var(--gold)" stroke-width=".8"><circle cx="5" cy="5" r="4.2"/><ellipse cx="5" cy="5" rx="1.8" ry="4.2"/><path d="M.8 5h8.4M1.5 3h7M1.5 7h7"/></svg>stillharbortonesoak.com</li>
      <li><svg viewBox="0 0 10 10"><path d="M5 .5a3.3 3.3 0 0 1 3.3 3.3C8.3 6 5 9.5 5 9.5S1.7 6 1.7 3.8A3.3 3.3 0 0 1 5 .5z" fill="var(--gold)"/><circle cx="5" cy="3.8" r="1.1" fill="var(--navy-mid)"/></svg>Southern, California</li>
    </ul>
  </div>

  <div class="panel panel--cover">
    <div class="photo" role="img" aria-label="Resort pool at night with cabanas, palms and guests floating for a sound bath"></div>
    <div class="abs brand" style="left:0;width:264px;top:52px;font-size:17px">STILL HARBOR<br><span style="font-size:10px">TONE SOAK</span></div>
    <h2 class="abs serif center" style="left:0;width:264px;top:132px;font-size:17px;line-height:20px;color:var(--text)">WELL-BEING<br>THAT TRANSFORMS</h2>
    <p class="abs center gold" style="left:0;width:264px;top:185px;font-size:8.3px;line-height:13px;letter-spacing:.03em">EXPERIENCES THAT ELEVATE<br>PEOPLE AND PERFORMANCE</p>
    <p class="abs center" style="left:0;width:264px;top:478px;font-size:7.8px;line-height:12.6px;letter-spacing:.02em;color:var(--text)">PREMIUM WELLNESS EXPERIENCES<br>FOR CORPORATE EVENTS AND RETREATS</p>
  </div>
</section>

<section class="spread spread--inside">
  <div class="photo bottom-photo" role="img" aria-label="Evening pool courtyard with candles and guests resting on floats"></div>
  <div class="photo side-photo" role="img" aria-label="Practitioner offering a towel treatment beside a pool"></div>

  <h2 class="abs serif section-title" style="left:22px;top:30px">WELLNESS<br>THAT WORKS<br><span class="gold">FOR YOU</span></h2>
  <div class="rule" style="left:22px;top:111px;width:33px"></div>
  <p class="abs body-copy" style="left:22px;top:129px;width:214px">Still Harbor Tone Soak brings immersive, science-informed wellness experiences to corporate events, conferences, and executive retreats across Southern California.</p>
  <p class="abs body-copy" style="left:22px;top:196px;width:202px">Our programs are designed to restore balance, enhance focus, and energize your most valuable asset-your people.</p>
  <div class="abs quote-mark" style="left:20px;top:246px">“</div>
  <p class="abs quote" style="left:56px;top:261px">When you invest in<br>well-being,<br>you elevate everything.</p>

  <div class="photo portrait" role="img" aria-label="Sound practitioner playing crystal instruments"></div>
  <h2 class="abs serif center gold" style="left:263px;width:264px;top:162px;font-size:14px;line-height:17.5px">DESIGNED FOR<br>HOSPITALITY PARTNERS</h2>
  <p class="abs center body-copy" style="left:263px;width:264px;top:202px;line-height:12px">We work within your space, schedule,<br>and operational needs. Professional, discreet, and<br>detail-oriented from start to finish. Experiences<br>customized for your audience<br>and event objectives. Local team. Local knowledge.<br>Trusted by premium brands and venues.</p>

  <h2 class="abs serif section-title" style="left:546px;top:30px">OUR<br>EXPERIENCES</h2>
  <div class="rule" style="left:546px;top:80px;width:33px"></div>

  <span class="service-icon" style="top:98px"></span>
  <h3 class="service-title" style="top:96px">RESET ROOMS</h3>
  <p class="service-copy" style="top:111px">Dedicated wellness spaces at conferences for on-demand relaxation and recovery.</p>
  <div class="sep" style="top:163px"></div>

  <span class="service-icon" style="top:180px"></span>
  <h3 class="service-title" style="top:178px">GUIDED MEDITATION</h3>
  <p class="service-copy" style="top:193px;width:100px">Calm the mind, reduce stress and improve clarity.</p>
  <div class="sep" style="top:238px"></div>

  <span class="service-icon" style="top:254px"></span>
  <h3 class="service-title" style="top:252px">BREATHWORK</h3>
  <p class="service-copy" style="top:267px;width:104px">Evidence-based techniques to energize, reset, and improve mental performance.</p>
  <div class="sep" style="top:326px"></div>

  <span class="service-icon" style="top:343px"></span>
  <h3 class="service-title" style="top:341px">YOGA AND<br>CHAIR YOGA</h3>
  <p class="service-copy" style="top:373px;width:96px">Gentle movement to relieve tension and support physical well-being.</p>

  <div class="rule" style="left:544px;top:437px;width:131px;background:var(--text-soft);opacity:.6"></div>
  <h2 class="abs serif cta-title">LETS CREATE SOMETHING<br>EXTRAORDINARY TOGETHER.</h2>
  <p class="abs cta-copy">Bring Still Harbor Tone Soak to your next event and create moments that <span class="gold">restore, inspire</span> and <span class="gold">elevate</span>.</p>
</section>

</body>
</html>
```